Kestrel Towbars Square Business Card Design

I would like a 2 x 2 square rounded corner business card.my business manufacture vehicle hitches and uses square tubing with rounded corners and would like to incorporate the border to look like the tubing...
2417 Larkmoor Ave. Boardman, Ohio 44512
(724) 390-6518
dale@kestreltowbars.com
www.kestreltowbars.com

Target Market(s)

automotive / vehicle hitches

Industry/Entity Type

Automotive

Contact Information for Business Card

I would like a 2 x 2 square rounded corner business card.my business manufacture vehicle hitches and uses square tubing with rounded corners and would like to incorporate the border to look like the tubing... and red, white and blue theme colors

Font styles to use
Sans Serif

Colors

Designer to choose colors to be used in the design.

Requirements
Must have
• Boarder
Nice to have
• red, white, blue theme colors
Should not have
• odd colors

```html
<!DOCTYPE html>
<html lang="en">
<head>
<meta charset="utf-8">
<title>Kestrel Towbars – Square Business Card</title>
<link rel="stylesheet" href="https://fonts.googleapis.com/css2?family=Arimo:wght@400;700&display=swap">
<style>
  :root {
    --backdrop: #a9aaae;
    --card-white: #ffffff;
    --flag-red: #e21d2d;
    --flag-navy: #1c3f7c;
  }
  html, body {
    margin: 0;
    padding: 0;
    width: 1200px;
    height: 1000px;
    overflow: hidden;
    background: var(--backdrop);
    font-family: "Arimo", Arial, sans-serif;
  }
  .canvas {
    position: relative;
    width: 1200px;
    height: 1000px;
  }
  .card {
    position: absolute;
    top: 290px;
    width: 422px;
    height: 422px;
    background: var(--card-white);
    border-radius: 52px;
  }
  .card--back { left: 165px; }
  .card--front { left: 651px; }

  .tube {
    position: absolute;
    box-sizing: border-box;
  }
  .tube--outer {
    inset: 13px;
    border-radius: 44px;
    padding: 24px;
  }
  .tube--inner {
    inset: 0;
    position: relative;
    border-radius: 30px;
    padding: 24px;
    height: 100%;
    outline: 2px solid var(--card-white);
    outline-offset: -2px;
  }
  .face {
    position: relative;
    height: 100%;
    background: var(--card-white);
    border-radius: 26px;
    display: flex;
    flex-direction: column;
    align-items: center;
    text-align: center;
  }
  .card--back .tube--outer { background: var(--flag-red); }
  .card--back .tube--inner { background: var(--flag-navy); }
  .card--front .tube--outer { background: var(--flag-navy); }
  .card--front .tube--inner { background: var(--flag-red); }

  .brand-name {
    margin: 0;
    color: var(--flag-navy);
    font-weight: 700;
    line-height: 1.05;
  }
  .card--back .brand-name {
    font-size: 38px;
    margin-top: 56px;
  }
  .card--front .face { justify-content: center; }
  .card--front .brand-name {
    font-size: 46px;
    margin-top: 40px;
  }
  .contact {
    margin: 34px 0 0;
    font-style: normal;
    color: var(--flag-navy);
    font-size: 16.5px;
    line-height: 20.8px;
  }
</style>
</head>
<body>
<main class="canvas">
  <section class="card card--back" aria-label="Card back with contact details">
    <div class="tube tube--outer">
      <div class="tube tube--inner">
        <div class="face">
          <h1 class="brand-name">Kestrel<br>Towbars</h1>
          <address class="contact">
            2417 Larkmoor Ave. Boardman,<br>
            Ohio 44512<br>
            (724) 390-6518<br>
            dale@kestreltowbars.com<br>
            www.kestreltowbars.com
          </address>
        </div>
      </div>
    </div>
  </section>

  <section class="card card--front" aria-label="Card front">
    <div class="tube tube--outer">
      <div class="tube tube--inner">
        <div class="face">
          <h2 class="brand-name">Kestrel<br>Towbars</h2>
        </div>
      </div>
    </div>
  </section>
</main>
</body>
</html>
```